Apply voucher for sale using a passer-by stopper (display on the street)

I have a photo studio (www.tomasvirkeland.eu) and would like to use my passer-by stopper (advertising display on the street) as an advertising medium for my photo shoot voucher sale - especially in the run-up to Christmas as a special gift idea. I thought of something funny like "You look 10 years younger in our light.
Give away a voucher and save a voucher value of € 150 - but only pay € 130. - so maybe - you must have a more interesting idea.
The poster should be in portrait format 60.5x86 cm (see picture below).

Target Market(s)

Consumer

Font styles to use
Serif

Colors

Designer to choose colors to be used in the design.

Requirements
Must have
• The passer-by stopper is intended to attract attention when driving or stopping driving. And, of course, encourage you to buy a voucher.
Nice to have
• No people need to be visible on the poster. But the poster should still
be emotional - maybe also Christmas.

```html
<!DOCTYPE html>
<html lang="de">
<head>
<meta charset="utf-8">
<title>Fotoshooting Gutschein – Tomas Virkeland Fotograf</title>
<link rel="stylesheet" href="https://fonts.googleapis.com/css2?family=Oswald:wght@200;300;500;700&family=Cinzel:wght@400&display=swap">
<style>
  :root {
    --paper: #ffffff;
    --ink: #111111;
    --ink-soft: #2a2a2a;
    --hair: #7a3a24;
    --hair-light: #a8522e;
    --veil: #7b4fa6;
    --veil-light: #9b73c4;
  }
  * { margin: 0; padding: 0; box-sizing: border-box; }
  html, body {
    width: 800px; height: 1200px; overflow: hidden;
    background: var(--paper);
  }
  .poster {
    position: relative;
    width: 800px; height: 1200px;
    background: var(--paper);
    overflow: hidden;
  }
  .portrait {
    position: absolute; left: 0; top: 0;
    width: 431px; height: 1200px;
    background:
      linear-gradient(180deg, var(--veil-light) 0%, var(--veil) 10%, var(--hair-light) 24%, #d9b3a3 40%, var(--hair) 62%, var(--hair-light) 80%, var(--veil) 100%);
  }
  .offer {
    position: absolute; left: 431px; top: 0;
    width: 369px; height: 1200px;
    text-align: center;
    color: var(--ink);
  }
  .headline {
    position: absolute; left: 0; right: 0; top: 62px;
    font-family: "Oswald", sans-serif;
    line-height: 1;
    text-transform: uppercase;
    white-space: nowrap;
  }
  .headline__bold {
    display: block;
    font-weight: 700;
    font-size: 116px;
    letter-spacing: -2px;
  }
  .headline__light {
    display: block;
    margin-top: 14px;
    font-weight: 200;
    font-size: 118px;
    letter-spacing: -2px;
  }
  .price-old {
    position: absolute; left: 0; right: 0; top: 372px;
    font-family: "Oswald", sans-serif;
    font-weight: 500;
    font-size: 44px;
    line-height: 1;
    color: var(--ink-soft);
  }
  .price-old span {
    position: relative; display: inline-block;
    transform: skewX(-8deg);
  }
  .price-old span::after {
    content: ""; position: absolute;
    left: -6px; right: -6px; top: 52%;
    height: 4px; background: var(--ink);
    transform: rotate(-4deg);
  }
  .price-new {
    position: absolute; left: 31px; top: 432px;
    width: 306px; height: 136px;
    background: var(--ink);
    color: var(--paper);
    font-family: "Oswald", sans-serif;
    font-weight: 700;
    font-size: 100px;
    line-height: 136px;
    letter-spacing: -1px;
  }
  .discount {
    position: absolute; left: 62px; top: 680px;
    width: 260px; height: 190px;
    font-family: "Oswald", sans-serif;
    font-weight: 700;
    color: var(--ink);
    text-align: left;
  }
  .discount__amount {
    position: absolute; left: 0; top: 0;
    font-size: 140px; line-height: 1;
    letter-spacing: -3px;
  }
  .discount__amount sup {
    font-size: 56px; vertical-align: top;
    position: relative; top: 14px; margin-left: 4px;
  }
  .discount__tag {
    position: absolute; left: 170px; top: 96px;
    width: 90px; height: 90px;
  }
  .brand {
    position: absolute; left: 0; right: 0; top: 930px;
    font-family: "Cinzel", serif;
    font-weight: 400;
    color: var(--ink);
    white-space: nowrap;
  }
  .brand__dot {
    display: block; margin: 0 auto;
    width: 80px; height: 80px;
    border: 3px solid var(--ink);
    border-radius: 50%;
  }
  .brand__name {
    display: block; margin-top: 26px;
    font-size: 30px; letter-spacing: 0;
  }
  .brand__role {
    display: block; margin-top: 6px;
    font-size: 16px; letter-spacing: 9px;
    padding-left: 9px;
  }
</style>
</head>
<body>
<main class="poster">
  <div class="portrait" role="img" aria-label="Portrait photograph of a young woman with long auburn hair wearing a purple lace headscarf"></div>

  <section class="offer">
    <h1 class="headline">
      <span class="headline__bold">Photo</span>
      <span class="headline__light">Shoot</span>
    </h1>

    <p class="price-old"><span>150€</span></p>
    <p class="price-new">130€</p>

    <div class="discount">
      <span class="discount__amount">20<sup>€</sup></span>
      <svg class="discount__tag" viewBox="0 0 90 90" aria-label="off">
        <g transform="rotate(-40 45 45)">
          <path d="M8 30 L26 18 L84 18 L84 72 L26 72 L8 60 Z" fill="var(--ink)"/>
          <circle cx="22" cy="45" r="5" fill="var(--paper)"/>
          <text x="57" y="54" text-anchor="middle" font-family="Oswald, sans-serif" font-weight="700" font-size="24" fill="var(--paper)">OFF</text>
        </g>
      </svg>
    </div>

    <div class="brand">
      <span class="brand__dot"></span>
      <span class="brand__name">Tomas Virkeland</span>
      <span class="brand__role">FOTOGRAF</span>
    </div>
  </section>
</main>
</body>
</html>
```